Photographic Tutorial website

We are looking for a fresh design for a photographic tutorial / workshop website. The website will have the included functions:

* Home (needs to have a login section)
* About Us
* Info about each course / workshop.
* Subscribe to courses and pay online.
* Members Area
* Photo gallery
* Contact us

The website will be implemented with our own made cms. We do not need it to be coded. We have a team ready to do this for us. We only need the PSD layout.

We have attached a mockup design that the client and I have come up with and we need the design to be taken to the next level.

Client also likes:
http://www.vellowindstudio.example/

Photographic Interests

Online

Requirements
Must have
• Must Stand out i.e black backgrounds
Should not have
• Alter the logo in anyway.

```html
<!DOCTYPE html>
<html lang="en">
<head>
<meta charset="utf-8">
<title>Aperture Mate – Photographic Tuition</title>
<link href="https://fonts.googleapis.com/css2?family=Oswald:wght@300;400;500&family=PT+Sans+Narrow:wght@400;700&family=Arimo:wght@400;700&display=swap" rel="stylesheet">
<style>
:root{
  --night:#1c1c1c;
  --paper:#e9e9e9;
  --ink:#222;
  --text:#444;
  --green:#3d9a3a;
  --btn:#1f7a12;
  --red:#c0140f;
  --band:#b5b5b5;
  --fb:#3b5590;
  --tw:#5ec3ec;
  --gp:#e8e8e8;
}
*{margin:0;padding:0;box-sizing:border-box}
html,body{width:1200px;height:1191px;overflow:hidden}
body{position:relative;background:var(--paper);font-family:"Arimo",Arial,sans-serif;color:var(--text)}
.abs{position:absolute}
.top-band{left:0;top:0;width:1200px;height:305px;background:var(--night)}
.rule{left:0;top:494px;width:1200px;height:1px;background:#d2d2d2}

.brand{left:133px;top:24px;display:flex;align-items:center;gap:10px}
.brand-dot{width:40px;height:40px;border-radius:50%;background:#2f4fa0}
.brand-name{font-family:"Oswald",sans-serif;font-weight:500;font-size:34px;color:#fff;letter-spacing:.5px}

.main-nav{left:547px;top:28px;width:522px;height:39px;border-top:1px solid #777;border-bottom:1px solid #777;display:flex}
.main-nav a{font-family:"PT Sans Narrow",sans-serif;font-size:17px;color:#fff;text-decoration:none;line-height:38px;padding:0 10px 0 10px}
.main-nav a.current{color:var(--green);background:#141414;padding:0 19px 0 10px;margin-right:9px}
.main-nav a+a{margin-left:9px}

.slider{left:131px;top:100px;width:938px;height:353px;background:#d6d6d6;border:1px solid #bdbdbd;border-radius:6px}
.slide-photo{left:7px;top:6px;width:924px;height:340px;background:linear-gradient(100deg,#6f9a3a 0%,#5d8a2a 30%,#2f5414 55%,#1e3a0d 75%,#3f6a1c 100%)}
.slide-copy{left:664px;top:166px;width:370px;color:#fff}
.slide-copy h1{font-family:"Oswald",sans-serif;font-weight:300;font-size:29px;line-height:35px;letter-spacing:.3px}
.slide-copy p{margin-top:12px;font-size:12px;line-height:17px;text-transform:uppercase}
.read-more{left:662px;top:346px;width:115px;height:35px;border-radius:7px;background:var(--btn);color:#fff;font-size:16px;line-height:35px;text-align:center}
.dots{left:979px;top:415px;display:flex;gap:6px}
.dots span{width:13px;height:13px;border-radius:50%;background:#bbb}
.dots span:first-child{background:#777;border:3px solid #bbb}

.tile{top:482px;width:205px;height:125px;box-shadow:0 6px 6px -3px rgba(0,0,0,.35);border:1px solid #999}
.tile b{position:absolute;left:0;right:0;bottom:6px;text-align:center;font-family:"Oswald",sans-serif;font-weight:400;font-size:15px;color:#fff}

.col-title{top:647px;font-family:"Oswald",sans-serif;font-weight:500;font-size:15px;color:var(--ink);letter-spacing:.2px}

.checklist{left:140px;top:686px}
.checklist h2{font-size:14px;font-weight:400;color:#111;margin-bottom:4px}
.checklist li{list-style:none;font-size:13px;line-height:18.8px;padding-left:15px;position:relative}
.checklist li::before{content:"→";position:absolute;left:0;font-size:9px;color:#666}

.map{left:458px;top:685px;width:219px;height:131px;background:linear-gradient(135deg,#e9e4d8,#ded8c6 60%,#cfe0b8);border:1px solid #ccc}
.loc-links{left:461px;top:820px;font-size:13px;line-height:17px;list-style:none}

.testimonials{left:772px;top:685px;width:298px;height:233px}
.quote{position:absolute;top:0;left:0;width:298px;height:233px;background:#fff;border:1px solid #ccc;border-radius:18px}
.notch{position:absolute;left:54px;top:-14px}
.person{position:absolute;left:15px}
.avatar{position:absolute;left:0;top:0;width:43px;height:41px;background:#c9bfb6;border:1px solid #aaa}
.who{position:absolute;left:55px;top:7px;white-space:nowrap}
.who strong{display:block;font-size:13px;color:#333}
.who em{display:block;font-style:normal;font-size:11px;color:var(--red);margin-top:3px}
.say{position:absolute;left:0;top:51px;width:280px;font-size:12px;line-height:15.5px;color:#333}
.divider{position:absolute;left:15px;top:104px;width:276px;height:1px;background:#ccc}

.partners{left:131px;top:939px;width:938px;height:81px;background:var(--band);border:1px solid #999;border-radius:3px}
.badge{position:absolute;background:#6d6d6d}

.footer{left:0;top:1045px;width:1200px;height:146px;background:linear-gradient(#2a2a2a,#000 45%)}
.credit{left:144px;top:1068px;font-size:12px;line-height:13px;color:#fff}
.follow{top:1067px;width:81px;height:25px;font-size:12px;line-height:25px;display:flex;align-items:center;gap:5px;padding-left:6px;border:1px solid #888}
.follow i{width:11px;height:11px;background:rgba(255,255,255,.8)}
.footer-brand{left:754px;top:1117px;display:flex;align-items:center;gap:8px}
.footer-brand span:first-child{width:30px;height:30px;border-radius:50%;background:#3a3a3a}
.footer-brand span:last-child{font-family:"Oswald",sans-serif;font-weight:500;font-size:27px;color:#4a4a4a}
</style>
</head>
<body>
<div class="abs top-band"></div>
<div class="abs rule"></div>

<header>
  <div class="abs brand"><span class="brand-dot"></span><span class="brand-name">Aperture Mate</span></div>
  <nav class="abs main-nav">
    <a class="current" href="#">HOME</a><a href="#">ABOUT US</a><a href="#">OUR COURSES</a><a href="#">MEMBER'S AREA</a><a href="#">CONTACT US</a>
  </nav>
</header>

<section class="abs slider">
  <div class="abs slide-photo" role="img" aria-label="Close-up photo of a green leaf and flower buds with water drops"></div>
</section>
<div class="abs slide-copy">
  <h1>LOREM IPSUM IS SIMPLY DUMMY</h1>
  <p>Lorem Ipsum is simply dummy text of the printing and typesetting industry. Lorem Ipsum has been the indus-try's standard dummy text ever since the 1500s, when an unknown printer took a galley of type and scrambled it to make a type specimen book.</p>
</div>
<div class="abs read-more">Read more</div>
<div class="abs dots"><span></span><span></span><span></span></div>

<div class="abs tile" style="left:131px;background:linear-gradient(#4a86c8,#a7b7c7 55%,#2c4a66)" role="img" aria-label="City skyline across a harbour"><b>URBAN</b></div>
<div class="abs tile" style="left:375px;background:linear-gradient(#8fb4dc,#e6e6e6 50%,#6a6a6a)" role="img" aria-label="Curved white building front"><b>PANORAMA</b></div>
<div class="abs tile" style="left:617px;background:linear-gradient(135deg,#3a1a10,#111 50%,#2a1a08)" role="img" aria-label="Illuminated shopping street sign at night"><b>CITY WALKS</b></div>
<div class="abs tile" style="left:859px;background:linear-gradient(#2a2a2a,#1a1a24 60%,#3a3020)" role="img" aria-label="City lights at night"><b>NIGHT PHOTOGRAPHY</b></div>

<h3 class="abs col-title" style="left:140px">MOON PHASE CHART</h3>
<h3 class="abs col-title" style="left:461px">LOCATION</h3>
<h3 class="abs col-title" style="left:790px">TESTIMONIALS</h3>

<div class="abs checklist">
  <h2>Photograpers check lists</h2>
  <ul>
    <li>Wedding shoot checklist</li><li>Pre shoot checklist</li><li>Standard checklist</li>
    <li>Pre shoot checklist</li><li>Standard checklist</li><li>Wedding shoot checklist</li>
  </ul>
</div>

<div class="abs map" role="img" aria-label="Street map of the studio location"></div>
<ul class="abs loc-links">
  <li>Photography Blog</li><li>General Infomationa</li><li>&amp; APM's 2012</li><li>USA Fall Tour</li><li>Traval Blog</li>
</ul>

<section class="abs testimonials">
  <div class="quote">
    <svg class="notch" width="36" height="16" viewBox="0 0 36 16"><path d="M0 0 L34 15 L8 15 Z" fill="#fff" stroke="#ccc"/><rect x="7" y="14" width="28" height="3" fill="#fff"/></svg>
    <div class="person" style="top:16px">
      <div class="avatar" role="img" aria-label="Portrait of Dorian Pell"></div>
      <div class="who"><strong>Dorian&nbsp; Pell</strong><em>CEO &amp; Co-Founder - Northwave.com</em></div>
      <p class="say">Renata is a founding member of Kestrel Partners. Prior to this, she was a Partner at Harbor Row</p>
    </div>
    <div class="divider"></div>
    <div class="person" style="top:116px">
      <div class="avatar" role="img" aria-label="Portrait of Milo Grant"></div>
      <div class="who"><strong>Milo Grant</strong><em>Founder - &nbsp;Brightlane.com</em></div>
      <p class="say">Proin viverra nunc a neque convallis ultricies eget euismod risus. Vivamus feugiat viverra tellus</p>
    </div>
  </div>
</section>

<section class="abs partners" aria-label="Partners">
  <div class="badge" style="left:31px;top:27px;width:123px;height:26px;border-radius:3px"></div>
  <div class="badge" style="left:205px;top:11px;width:56px;height:56px;border-radius:50%"></div>
  <div class="badge" style="left:320px;top:15px;width:50px;height:50px;border-radius:4px"></div>
  <div class="badge" style="left:431px;top:27px;width:123px;height:26px;border-radius:3px"></div>
  <div class="badge" style="left:605px;top:11px;width:56px;height:56px;border-radius:50%"></div>
  <div class="badge" style="left:720px;top:15px;width:50px;height:50px;border-radius:4px"></div>
  <div class="badge" style="left:841px;top:11px;width:56px;height:56px;border-radius:50%"></div>
</section>

<footer>
  <div class="abs footer"></div>
  <p class="abs credit">Website by<br>Coastline Web Studio @2012</p>
  <div class="abs follow" style="left:808px;background:var(--fb);color:#fff"><i></i>Follow us</div>
  <div class="abs follow" style="left:894px;background:var(--tw);color:#fff"><i></i>Follow us</div>
  <div class="abs follow" style="left:979px;background:var(--gp);color:#777"><i style="background:#999"></i>Follow us</div>
  <div class="abs footer-brand"><span></span><span>Aperture Mate</span></div>
</footer>
</body>
</html>
```